依頼詳細
定期的に開催する譲渡会イベントのチラシを会場周辺の住宅等に配布し、保護犬の存在を知らない人にも知って頂けるようにチラシ作成(A4サイズ)のご協力をお願い致します。
記載項目
イベントタイトル ⇒ ほほえみ巡りの道
愛犬同伴可能・入場料無料
開催日時 ⇒ ●年●月●日(●)●時~●時
開催会場 ⇒ Sunny Pawz 東大阪会場 (住所:●●●●)
開催内容 ⇒ 保護犬の新しいお家探し
トリマーによるワンコインお手入れ
わんちゃん用品フリマ販売
わんちゃんオリジナルプリントグッズ受注会(※1)
注意事項 ⇒ 当日の参加犬はInstagramにてご確認お願い致します。
イベント内容は変更になる場合があります。
愛犬同伴の場合、マナー用品の着用をお願い致します。
会場が狭いため、入場制限を行う場合がございます。
検温・アルコール消毒・マスク着用のご協力をお願い致します。
主催 ⇒ 特定非営利活動法人Sunny Pawz
〒579-2208 枚方市桜木台四丁目3番21号
HP https://sunnypawz2019.example-site.jp/
Instagram sunnypawz.2019
サイズ
A4
ページ数
片面
希望イメージ
シンプル 複雑
単色 カラフル
暗い 明るい
日常 高級
遊び心 厳粛
未来的 伝統的
女性的 男性的
希望する色
カラフル
納品ファイル
• 高解像度JPG (.jpg)
• イラストレーター形式 (.ai)
補足説明
開催日時・会場は、イベントごとに変更して使用させて頂きたいと思っていますので、標準的なフォントでの作成をお願い致します。
その他、フリーイラストやフリー写真を使用して頂いて大丈夫です。

記載内容追加
開催内容の一番最後に、当日の売上金は保護犬の活動費となります。(※1については一部)
ホームページ・InstagramのQRコード記載をお願い致します。
■ 選んだ理由

文字と写真(イラスト)のバランスや、お伝え出来ていなかったカラーイメージも、当団体のSNS等を拝見してくださって作って頂けたのかなと思い、とても嬉しくなりました。
スタッフ全員での選考を行い、全員が気に入ったため、こちらの提案を当選とさせて頂きました。
度重なる修正依頼にも迅速にご対応頂けて、とても感謝しております。

■ 提案者全員のお礼・コメント

この度、ご提案頂きました皆様、本当にありがとうございました。
皆様の技術のお力をお借りするのに、十分とは言えない金額だったにも関わらず、沢山のご提案を頂けましたこと、感謝しております。

```html
<!DOCTYPE html>
<html lang="ja">
<head>
<meta charset="utf-8">
<title>ほほえみ巡りの道 保護犬譲渡会</title>
<link href="https://fonts.googleapis.com/css2?family=M+PLUS+Rounded+1c:wght@400;700;800;900&display=swap" rel="stylesheet">
<style>
:root{
  --bg-outer:#f7a823;
  --bg-inner:#fff7cf;
  --pink:#ea4f8c;
  --red:#e4362c;
  --blue:#2f86d1;
  --navy:#23406e;
  --brown:#5a3a1a;
  --white:#ffffff;
  --dog:#d9a066;
  --dog-light:#f0c890;
  --ink:#222222;
}
*{margin:0;padding:0;box-sizing:border-box}
html,body{width:852px;height:1200px;overflow:hidden}
body{font-family:"M PLUS Rounded 1c",sans-serif;background:var(--bg-outer);color:var(--brown);position:relative}
.sheet{position:absolute;left:12px;top:12px;width:828px;height:1176px;background:var(--bg-inner);border-radius:28px;border:4px dashed #fbd36a}
.abs{position:absolute}
.org-label{left:0;right:0;top:112px;text-align:center;font-size:18px;font-weight:700;color:var(--brown)}
.org-name{left:0;right:0;top:160px;text-align:center;font-size:88px;font-weight:900;color:var(--pink);letter-spacing:2px;line-height:1}
.illust{border-radius:50%;background:radial-gradient(circle at 45% 40%,var(--dog-light),var(--dog))}
.badge{border-radius:50%;background:var(--red);color:var(--white);display:flex;align-items:center;justify-content:center;text-align:center;font-weight:900;line-height:1.25}
.badge-pets{left:58px;top:258px;width:120px;height:120px;font-size:20px;transform:rotate(-8deg)}
.badge-free{left:672px;top:236px;width:120px;height:120px;font-size:24px;transform:rotate(8deg)}
.subtitle{left:0;right:0;top:404px;text-align:center;font-size:24px;font-weight:800;color:var(--navy)}
.title-band{left:96px;right:96px;top:444px;height:92px;background:var(--red);border-radius:46px;color:var(--white);font-size:62px;font-weight:900;display:flex;align-items:center;justify-content:center;letter-spacing:4px}
.venue{left:0;right:0;top:566px;text-align:center;font-size:34px;font-weight:900;color:var(--red)}
.venue-addr{left:0;right:0;top:616px;text-align:center;font-size:15px;font-weight:700;color:var(--brown)}
.date-band{left:0;right:0;top:650px;height:62px;background:var(--blue);color:var(--white);font-size:38px;font-weight:900;display:flex;align-items:center;justify-content:center;letter-spacing:3px}
.lead{left:44px;top:736px;font-size:40px;font-weight:900;color:var(--pink);line-height:1.2}
.lead small{font-size:30px;color:var(--navy)}
.menu{left:50px;top:800px;list-style:none;font-size:23px;font-weight:800;color:var(--red);line-height:1.5}
.menu li::before{content:"●";color:var(--pink);margin-right:6px;font-size:16px}
.menu .note{font-size:11px;color:var(--brown);font-weight:700;margin-left:6px}
.notes{left:60px;top:942px;width:510px;padding:12px 18px;background:var(--white);border-radius:16px;font-size:12.5px;font-weight:700;line-height:1.7;color:var(--brown)}
.proceeds{left:600px;top:948px;width:216px;padding:10px;background:var(--white);border:3px solid var(--pink);border-radius:12px;font-size:15px;font-weight:800;color:var(--pink);line-height:1.45;text-align:center}
.proceeds small{display:block;font-size:11px;color:var(--brown)}
.footer{left:50px;top:1094px;color:var(--brown)}
.footer .host{font-size:20px;font-weight:900;color:var(--navy);line-height:1.3}
.footer p{font-size:13px;font-weight:700;line-height:1.5}
.qr{width:72px;height:72px;background:var(--white);border:3px solid var(--ink);border-radius:4px}
.qr-label{width:90px;text-align:center;font-size:11px;font-weight:700;color:var(--brown)}
</style>
</head>
<body>
<div class="sheet"></div>

<div class="abs illust" style="left:30px;top:30px;width:120px;height:110px" role="img" aria-label="dog illustration, top left"></div>
<div class="abs illust" style="left:690px;top:110px;width:130px;height:160px" role="img" aria-label="dog illustration, top right"></div>

<div class="abs org-label">特定非営利活動法人</div>
<div class="abs org-name">Sunny Pawz</div>

<div class="abs badge badge-pets">愛犬同伴<br>OKです!</div>
<div class="abs badge badge-free">入場料<br>無料</div>

<div class="abs subtitle">保護犬譲渡会</div>
<div class="abs title-band">ほほえみ巡りの道</div>

<div class="abs illust" style="left:28px;top:520px;width:120px;height:110px" role="img" aria-label="dog illustration, left"></div>
<div class="abs illust" style="left:700px;top:520px;width:120px;height:110px" role="img" aria-label="dog illustration, right"></div>

<div class="abs venue">会場:Sunny Pawz 東大阪会場</div>
<div class="abs venue-addr">大阪府東大阪市●●●●</div>

<div class="abs date-band">●年●月●日【●】●時~●時</div>

<div class="abs lead"><small>保護犬の</small>新しいお家探し</div>
<ul class="abs menu">
  <li>トリマーによるワンコインお手入れ</li>
  <li>わんちゃん用品フリマ販売<span class="note">中古品や手作り用品の販売</span></li>
  <li>わんちゃんオリジナルプリントグッズ受注会※1</li>
</ul>

<div class="abs illust" style="left:640px;top:730px;width:170px;height:200px" role="img" aria-label="large dog illustration"></div>

<div class="abs notes">
当日の参加犬はInstagramにてご確認お願い致します。<br>
イベント内容は変更になる場合があります。<br>
愛犬同伴の場合、マナー用品の着用をお願い致します。<br>
会場が狭いため、入場制限を行う場合がございます。<br>
検温・アルコール消毒・マスク着用のご協力をお願い致します。
</div>

<div class="abs proceeds">当日の売上金は保護犬の活動費となります。<small>(※1については一部)</small></div>

<div class="abs footer">
  <div class="host">主催:特定非営利活動法人Sunny Pawz</div>
  <p>〒579-2208 枚方市桜木台四丁目3番21号</p>
  <p>HP https://sunnypawz2019.example-site.jp/</p>
  <p>Instagram sunnypawz.2019</p>
</div>

<div class="abs qr" style="left:640px;top:1070px" role="img" aria-label="homepage QR code"></div>
<div class="abs qr-label" style="left:631px;top:1148px">ホームページ</div>
<div class="abs qr" style="left:740px;top:1070px" role="img" aria-label="Instagram QR code"></div>
<div class="abs qr-label" style="left:731px;top:1148px">インスタグラム</div>
</body>
</html>
```